Gestaltung Deutschlandfahne
Zielgruppe
Korvexa Verkäufer / Korvexa Käufer
Aufgabenstellung
Gestaltung einer Deutschlandfahne.
Frei in der Gestaltung nach vorgegebener Skizze

```html
<!DOCTYPE html>
<html lang="de">
<head>
<meta charset="utf-8">
<title>Deutschlandfahne 2024</title>
<link rel="stylesheet" href="https://fonts.googleapis.com/css2?family=Arimo:wght@700&display=swap">
<style>
  :root {
    --paper: #fefefe;
    --flag-black: #030402;
    --flag-red: #dc0c15;
    --flag-gold: #fccf00;
    --star: #fcd600;
    --text-light: #ffffff;
    --ball-light: #ffffff;
    --ball-shade: #d9d9d9;
    --ball-edge: #000000;
    --shadow-soft: rgba(120, 100, 30, 0.35);
    --shadow-core: #332f1c;
  }
  html, body {
    margin: 0;
    padding: 0;
    overflow: hidden;
    background: var(--paper);
  }
  .canvas {
    position: relative;
    width: 1200px;
    height: 1200px;
    background: var(--paper);
    overflow: hidden;
  }
  .flag {
    position: absolute;
    left: 64px;
    top: 302px;
    width: 1077px;
    height: 572px;
    display: flex;
    flex-direction: column;
  }
  .flag__band { width: 100%; }
  .flag__band--black { height: 192px; background: var(--flag-black); }
  .flag__band--red { height: 188px; background: var(--flag-red); }
  .flag__band--gold { height: 192px; background: var(--flag-gold); }
  .flag__year {
    position: absolute;
    left: 0;
    width: 100%;
    top: 356px;
    margin: 0;
    text-align: center;
    font-family: "Arimo", Arial, sans-serif;
    font-weight: 700;
    font-size: 78px;
    line-height: 1;
    letter-spacing: 2px;
    color: var(--text-light);
    transform: translateX(-8px);
  }
  .artwork {
    position: absolute;
    left: 0;
    top: 0;
    width: 1200px;
    height: 1200px;
  }
  .star { fill: var(--star); }
  .ball-shadow__soft { fill: var(--shadow-soft); }
  .ball-shadow__core { fill: var(--shadow-core); }
  .ball { stroke: var(--ball-edge); stroke-width: 6; }
</style>
</head>
<body>
<main class="canvas">
  <section class="flag" aria-label="Deutschlandfahne">
    <div class="flag__band flag__band--black"></div>
    <div class="flag__band flag__band--red"></div>
    <div class="flag__band flag__band--gold"></div>
  </section>
  <h1 class="flag__year">2024</h1>

  <svg class="artwork" viewBox="0 0 1200 1200" xmlns="http://www.w3.org/2000/svg">
    <defs>
      <polygon id="star-shape" points="0,-45 12,-13 48,-12 19,10 30,45 0,24 -30,45 -19,10 -48,-12 -12,-13"/>
      <radialGradient id="ball-fill" cx="0.4" cy="0.35" r="0.7">
        <stop offset="0.6" stop-color="var(--ball-light)"/>
        <stop offset="1" stop-color="var(--ball-shade)"/>
      </radialGradient>
    </defs>

    <g class="stars stars--left">
      <use href="#star-shape" class="star" x="185" y="588"/>
      <use href="#star-shape" class="star" x="323" y="588"/>
    </g>
    <g class="stars stars--right">
      <use href="#star-shape" class="star" x="876" y="588"/>
      <use href="#star-shape" class="star" x="1015" y="588"/>
    </g>

    <g class="ball-shadow">
      <ellipse class="ball-shadow__soft" cx="602" cy="836" rx="138" ry="19"/>
      <ellipse class="ball-shadow__core" cx="602" cy="836" rx="86" ry="12"/>
    </g>

    <circle class="ball" cx="602" cy="634" r="176" fill="url(#ball-fill)"
            role="img" aria-label="Illustration eines schwarz-weißen Fußballs"/>
  </svg>
</main>
</body>
</html>
```